Brimovex business card

Based on company logo and website given , to design a business card temple. Slogan "Your furry friends deserves the best"
Color style please refer to our website

```html
<!DOCTYPE html>
<html lang="en">
<head>
<meta charset="utf-8">
<title>Brimovex business card</title>
<link rel="stylesheet" href="https://fonts.googleapis.com/css2?family=Manrope:wght@400;500;800&display=swap">
<style>
  :root {
    --backdrop: #267f97;
    --card-olive: #bdae2f;
    --card-white: #ffffff;
    --ink: #231f20;
    --paw-olive-tone: #a99b2a;
    --paw-grey-tone: #ececec;
  }
  * { margin: 0; padding: 0; box-sizing: border-box; }
  html, body {
    width: 1200px;
    height: 800px;
    overflow: hidden;
  }
  body {
    background: var(--backdrop);
    position: relative;
    font-family: "Manrope", sans-serif;
    color: var(--ink);
  }
  .card {
    position: absolute;
    top: 89px;
    width: 356px;
    height: 622px;
  }
  .card--front { left: 175px; background: var(--card-olive); }
  .card--back  { left: 640px; background: var(--card-white); }

  .brand-name {
    position: absolute;
    left: 0;
    width: 100%;
    text-align: center;
    font-family: "Manrope", sans-serif;
    font-weight: 800;
    font-size: 62px;
    letter-spacing: -1px;
    line-height: 1;
    color: var(--ink);
  }
  .card--front .brand-name { top: 236px; }
  .card--back .brand-name  { top: 86px; }

  .contact-list {
    position: absolute;
    left: 47px;
    top: 214px;
    list-style: none;
  }
  .contact-item {
    display: flex;
    align-items: center;
    height: 30px;
    margin-bottom: 15.5px;
    font-size: 20px;
    font-weight: 400;
    letter-spacing: -0.2px;
    white-space: nowrap;
  }
  .contact-icon {
    width: 30px;
    height: 30px;
    flex: none;
    margin-right: 21px;
  }

  .paw-trail {
    position: absolute;
    top: 432px;
    width: 92px;
    height: 178px;
    border-radius: 46px;
  }
  .card--front .paw-trail { left: 16px; background: var(--paw-olive-tone); }
  .card--back .paw-trail  { left: 245px; background: var(--paw-grey-tone); }
</style>
</head>
<body>

  <section class="card card--front" aria-label="Card front">
    <h1 class="brand-name">Brimovex</h1>
    <div class="paw-trail" role="img" aria-label="Trail of dark paw prints"></div>
  </section>

  <section class="card card--back" aria-label="Card back">
    <h2 class="brand-name">Brimovex</h2>

    <ul class="contact-list">
      <li class="contact-item">
        <svg class="contact-icon" viewBox="0 0 30 30" aria-hidden="true">
          <circle cx="15" cy="15" r="15" fill="var(--ink)"/>
          <path d="M10.5 8.5c.6-.5 1.4-.4 1.8.2l1.4 2.2c.4.6.2 1.3-.3 1.7l-.9.6c.7 1.8 2 3.1 3.8 3.8l.6-.9c.4-.5 1.1-.7 1.7-.3l2.2 1.4c.6.4.7 1.2.2 1.8l-1 1.2c-.6.7-1.6.9-2.5.6-4-1.5-6.9-4.4-8.4-8.4-.3-.9-.1-1.9.6-2.5z" fill="#fff"/>
        </svg>
        +41 22 57 80 913
      </li>
      <li class="contact-item">
        <svg class="contact-icon" viewBox="0 0 30 30" aria-hidden="true">
          <circle cx="15" cy="15" r="15" fill="var(--ink)"/>
          <rect x="7" y="9.5" width="16" height="11" fill="none" stroke="#fff" stroke-width="1.5"/>
          <path d="M7 9.5l8 6.5 8-6.5M7 20.5l6-5M23 20.5l-6-5" fill="none" stroke="#fff" stroke-width="1.3"/>
        </svg>
        hello@brimovex-mail.com
      </li>
      <li class="contact-item">
        <svg class="contact-icon" viewBox="0 0 30 30" aria-hidden="true">
          <circle cx="15" cy="15" r="15" fill="var(--ink)"/>
          <circle cx="15" cy="15" r="8" fill="none" stroke="#fff" stroke-width="1.5"/>
          <ellipse cx="15" cy="15" rx="3.5" ry="8" fill="none" stroke="#fff" stroke-width="1.2"/>
          <path d="M7 15h16" stroke="#fff" stroke-width="1.2"/>
        </svg>
        www.brimovex-pets.com
      </li>
      <li class="contact-item">
        <svg class="contact-icon" viewBox="0 0 30 30" aria-hidden="true">
          <circle cx="15" cy="15" r="15" fill="var(--ink)"/>
          <path d="M15 6.5a6 6 0 0 1 6 6c0 4.3-6 11-6 11s-6-6.7-6-11a6 6 0 0 1 6-6z" fill="#fff"/>
          <circle cx="15" cy="12.5" r="2.2" fill="var(--ink)"/>
        </svg>
        Place Name, Country
      </li>
    </ul>

    <div class="paw-trail" role="img" aria-label="Trail of light grey paw prints"></div>
  </section>

</body>
</html>
```